Varnel Consulting needs a business card design

Varnel Consulting is a small business that consults and trains Australia wide in Workplace Health and Safety, Environment and Quality Management Systems.

Clients are typically smaller businesses with 50 to 200 employees but there are some large clients.

Communication is often by email, although mobile is used as well.

Varnel Consulting
61 Tormoth Vale Road
Pellowby, QLD 4391
0438 912 047

```html
<!DOCTYPE html>
<html lang="en">
<head>
<meta charset="utf-8">
<title>Varnel Consulting — Business Card</title>
<link rel="stylesheet" href="https://fonts.googleapis.com/css2?family=Parisienne&display=swap">
<style>
  :root {
    --card-black: #0a0b0b;
    --brand-red: #8a1010;
    --text-cream: #f4f1ea;
    --glow-orange: #f26a1b;
    --glow-cream: #fbf3c4;
  }
  html, body {
    margin: 0;
    padding: 0;
    width: 1200px;
    height: 686px;
    overflow: hidden;
    background: var(--card-black);
  }
  .card {
    position: relative;
    width: 1200px;
    height: 686px;
    background: var(--card-black);
    font-family: "Parisienne", cursive;
  }
  .company-name {
    position: absolute;
    left: 138px;
    top: 100px;
    margin: 0;
    font-weight: 400;
    font-size: 82px;
    line-height: 1.2;
    color: var(--brand-red);
    white-space: nowrap;
  }
  .contact {
    position: absolute;
    left: 100px;
    top: 412px;
    width: 540px;
    margin: 0;
    font-style: normal;
    font-size: 36px;
    line-height: 54px;
    color: var(--text-cream);
    text-align: center;
    white-space: nowrap;
  }
  .contact .label {
    color: var(--brand-red);
  }
  .bulb-illustration {
    position: absolute;
    left: 770px;
    top: 100px;
    width: 320px;
    height: 420px;
    border-radius: 50%;
    background: radial-gradient(ellipse at 50% 55%,
      rgba(251, 243, 196, 0.28) 0%,
      rgba(242, 106, 27, 0.18) 35%,
      rgba(242, 106, 27, 0.06) 60%,
      rgba(10, 11, 11, 0) 75%);
  }
</style>
</head>
<body>
  <main class="card">
    <h1 class="company-name">Varnel Consulting</h1>
    <address class="contact">
      <span class="label">Adress</span> : 61 Tormoth Vale Road<br>
      Pellowby, QLD 4391<br>
      <span class="label">tel</span>:&nbsp; 0438 912 047
    </address>
    <div class="bulb-illustration" role="img" aria-label="Glowing line-drawn light bulb in orange fading to cream"></div>
  </main>
</body>
</html>
```